Business Cards / Stationary
Harlow Defense Firm
Project: Business Cards / Stationary
Business Cards / Stationary - Law
Creative Brief
Professional
Gareth P. Harlow
Attorney and Counselor
248 N. Kestrel Court Suite 305 Denton, Texas 76209
gareth@garethharlowlaw.example
www.garethharlowlaw.example
I dont have to have front and back but would like to see concept with Blue logo on back side of card

```html
<!DOCTYPE html>
<html lang="en">
<head>
<meta charset="utf-8">
<title>Harlow Defense Firm – Business Cards</title>
<link href="https://fonts.googleapis.com/css2?family=Open+Sans:wght@400;600&display=swap" rel="stylesheet">
<style>
  :root {
    --navy: #1d2a78;
    --navy-deep: #16205f;
    --gold: #f2c318;
    --paper: #ffffff;
    --paper-shade: #eef0f3;
    --ink: #4a4f5a;
    --rule: #8a8f99;
    --backdrop: #e6e7ea;
  }
  * { margin: 0; padding: 0; box-sizing: border-box; }
  html, body { width: 1200px; height: 904px; overflow: hidden; }
  body {
    background: var(--backdrop);
    font-family: "Open Sans", Arial, sans-serif;
    position: relative;
  }
  .card {
    position: absolute;
    width: 560px;
    height: 320px;
    border-radius: 14px;
    overflow: hidden;
    box-shadow: 0 10px 30px rgba(0,0,0,.18);
  }
  /* Back side */
  .card--back {
    left: 110px; top: 90px;
    background: linear-gradient(135deg, var(--navy) 0%, var(--navy-deep) 100%);
    display: flex; align-items: center; justify-content: center;
  }
  .wordmark { display: flex; align-items: center; gap: 10px; }
  .wordmark__dot {
    width: 34px; height: 34px; border-radius: 50%;
    border: 2px solid currentColor;
  }
  .wordmark__name {
    font-weight: 600; letter-spacing: .06em; text-transform: uppercase;
    font-size: 20px;
  }
  .card--back .wordmark { color: var(--paper); }

  /* Front side */
  .card--front {
    left: 530px; top: 484px;
    background: linear-gradient(160deg, var(--paper) 55%, var(--paper-shade) 100%);
  }
  .card--front .wordmark {
    position: absolute; left: 34px; top: 40px; color: var(--navy);
  }
  .card--front .wordmark__dot { width: 30px; height: 30px; }
  .card--front .wordmark__name { font-size: 17px; }
  .identity {
    position: absolute; right: 34px; top: 40px; text-align: right;
  }
  .identity__name { color: var(--navy); font-weight: 600; font-size: 16px; }
  .identity__title { color: var(--ink); font-size: 12px; margin-top: 3px; }
  .divider {
    position: absolute; left: 34px; right: 34px; top: 100px;
    height: 1px; background: var(--rule);
  }
  .contact {
    position: absolute; left: 36px; top: 196px;
    color: var(--ink); font-size: 11.5px; line-height: 1.45;
  }
  .contact__address { margin-bottom: 6px; }
  .contact__row { display: flex; align-items: center; gap: 7px; }
  .contact__row svg { width: 11px; height: 11px; fill: var(--ink); flex: none; }
  .band-gold {
    position: absolute; left: 0; bottom: 0; width: 62%; height: 9px;
    background: var(--gold);
  }
  .band-navy {
    position: absolute; right: 0; bottom: 0; width: 300px; height: 36px;
  }
  .band-navy svg { position: absolute; inset: 0; }
  .band-navy__url {
    position: absolute; right: 22px; bottom: 11px;
    color: var(--paper); font-size: 11.5px; letter-spacing: .08em;
  }
</style>
</head>
<body>
  <section class="card card--back" aria-label="Card back">
    <div class="wordmark">
      <span class="wordmark__dot"></span>
      <span class="wordmark__name">Harlow Defense Firm</span>
    </div>
  </section>

  <section class="card card--front" aria-label="Card front">
    <div class="wordmark">
      <span class="wordmark__dot"></span>
      <span class="wordmark__name">Harlow Defense Firm</span>
    </div>
    <div class="identity">
      <p class="identity__name">Gareth P. Harlow</p>
      <p class="identity__title">Attorney and Counselor</p>
    </div>
    <div class="divider"></div>

    <div class="contact">
      <p class="contact__address">248 N. Kestrel Court Suite 305<br>Denton, Texas 76209</p>
      <p class="contact__row">
        <svg viewBox="0 0 24 24"><path d="M6.6 10.8a15.1 15.1 0 0 0 6.6 6.6l2.2-2.2a1 1 0 0 1 1-.25 11.4 11.4 0 0 0 3.6.57 1 1 0 0 1 1 1V20a1 1 0 0 1-1 1A17 17 0 0 1 3 4a1 1 0 0 1 1-1h3.5a1 1 0 0 1 1 1c0 1.25.2 2.45.57 3.57a1 1 0 0 1-.25 1z"/></svg>
        940-555-0142
      </p>
      <p class="contact__row">
        <svg viewBox="0 0 24 24"><path d="M7 2h10a2 2 0 0 1 2 2v16a2 2 0 0 1-2 2H7a2 2 0 0 1-2-2V4a2 2 0 0 1 2-2zm0 3v13h10V5zm5 14.2a1 1 0 1 0 0 .01z"/></svg>
        940-555-0178
      </p>
      <p class="contact__row">
        <svg viewBox="0 0 24 24"><path d="M3 5h18a1 1 0 0 1 1 1v12a1 1 0 0 1-1 1H3a1 1 0 0 1-1-1V6a1 1 0 0 1 1-1zm1 2.3V17h16V7.3l-8 5.2z"/></svg>
        gareth@garethharlowlaw.example
      </p>
    </div>

    <div class="band-gold"></div>
    <div class="band-navy">
      <svg viewBox="0 0 300 36" preserveAspectRatio="none"><path d="M22 0H300V36H0Q6 0 22 0Z" fill="var(--navy)"/></svg>
      <span class="band-navy__url">www.garethharlowlaw.example</span>
    </div>
  </section>
</body>
</html>
```